Business Card Design

We need a business card design for a new company called Riverbend Advisory, LLC. We are a project management and software engineering consulting company. We prefer to use blues but am open to any colors. We would like out design to show strength and creativity.

I've uploaded new logo designs to the project.  Please use these logo designs for the business card. Thanks!

Industry/Entity Type

Software

Contact Information for Business Card

Daniel Whitford
Consultant
Owner

Riverbend Advisory, LLC

2716 5th St. S #4372
Arlington, VA 22198

703-555-0187
dwhitford@rvbadv.example
www.rvbadv.example

```html
<!DOCTYPE html>
<html lang="en">
<head>
<meta charset="utf-8">
<title>Riverbend Advisory – Business Card</title>
<link href="https://fonts.googleapis.com/css2?family=Oswald:wght@500&family=Lato:wght@400;700&display=swap" rel="stylesheet">
<style>
  :root {
    --navy: #0f3d5c;
    --orange: #e2481f;
    --white: #ffffff;
    --paper: #f4f4f2;
    --stage: #e6e4df;
  }
  html, body {
    margin: 0;
    padding: 0;
    width: 1200px;
    height: 1024px;
    overflow: hidden;
    background: var(--stage);
  }
  .canvas {
    position: relative;
    width: 1200px;
    height: 1024px;
  }
  .card {
    position: absolute;
    left: 210px;
    width: 780px;
    height: 446px;
    overflow: hidden;
    box-shadow: 0 6px 18px rgba(0,0,0,0.18);
  }
  .card-front { top: 48px; background: var(--paper); }
  .card-back  { top: 530px; background: var(--navy); }

  .card-shapes { position: absolute; inset: 0; }

  /* Front */
  .brand-name {
    position: absolute;
    left: 64px;
    top: 60px;
    margin: 0;
    font-family: "Lato", sans-serif;
    font-weight: 700;
    font-size: 34px;
    line-height: 1.1;
    letter-spacing: 1px;
    text-transform: uppercase;
    color: var(--navy);
  }
  .person {
    position: absolute;
    right: 56px;
    top: 92px;
    text-align: left;
  }
  .person-name {
    margin: 0;
    font-family: "Oswald", sans-serif;
    font-weight: 500;
    font-size: 34px;
    color: var(--white);
    line-height: 1.1;
  }
  .person-title {
    margin: 4px 0 0;
    font-family: "Lato", sans-serif;
    font-size: 18px;
    color: var(--orange);
  }
  .contact-list {
    position: absolute;
    left: 64px;
    top: 262px;
    margin: 0;
    padding: 0;
    list-style: none;
    font-family: "Lato", sans-serif;
    font-size: 19px;
    color: var(--white);
  }
  .contact-item {
    display: flex;
    align-items: flex-start;
    gap: 16px;
    margin-bottom: 9px;
    line-height: 1.3;
  }
  .contact-icon { flex: none; width: 20px; height: 20px; margin-top: 2px; }
  .accent { color: var(--orange); }

  /* Back */
  .web-band {
    position: absolute;
    left: 92px;
    top: 0;
    width: 50px;
    height: 100%;
    background: var(--orange);
  }
  .web-band-text {
    position: absolute;
    left: 50%;
    top: 50%;
    transform: translate(-50%, -50%) rotate(-90deg);
    white-space: nowrap;
    font-family: "Lato", sans-serif;
    font-size: 17px;
    letter-spacing: 6px;
    color: var(--white);
  }
  .back-brand {
    position: absolute;
    left: 240px;
    top: 170px;
    margin: 0;
    font-family: "Lato", sans-serif;
    font-weight: 700;
    font-size: 50px;
    line-height: 1.1;
    letter-spacing: 2px;
    text-transform: uppercase;
    color: var(--white);
  }
</style>
</head>
<body>
<main class="canvas">

  <section class="card card-front" aria-label="Business card front">
    <svg class="card-shapes" width="780" height="446" viewBox="0 0 780 446" aria-hidden="true">
      <path fill="var(--orange)" d="M0,206 C160,204 270,158 350,88 C410,36 450,-22 520,-22 L780,-22 L780,446 L0,446 Z"/>
      <path fill="var(--white)" d="M0,222 C160,220 270,174 350,104 C410,52 450,-6 520,-6 L780,-6 L780,446 L0,446 Z"/>
      <path fill="var(--navy)" d="M0,228 C160,226 270,180 350,110 C410,58 450,0 520,0 L780,0 L780,446 L0,446 Z"/>
    </svg>

    <p class="brand-name">Riverbend<br>Advisory</p>

    <div class="person">
      <h1 class="person-name">Daniel Whitford</h1>
      <p class="person-title">Consultant / Owner</p>
    </div>

    <ul class="contact-list">
      <li class="contact-item">
        <svg class="contact-icon" viewBox="0 0 20 20" aria-hidden="true"><path fill="var(--orange)" d="M5 2l3 4-2 2c1 2.5 3 4.5 5.5 5.5l2-2 4 3-2 3C9 17 3 11 2 4z"/></svg>
        <span>703-555-0187</span>
      </li>
      <li class="contact-item">
        <svg class="contact-icon" viewBox="0 0 20 20" aria-hidden="true"><circle cx="10" cy="10" r="9" fill="var(--orange)"/><rect x="5" y="7" width="10" height="7" fill="none" stroke="var(--navy)" stroke-width="1.4"/><path d="M5 7l5 4 5-4" fill="none" stroke="var(--navy)" stroke-width="1.4"/></svg>
        <span>dwhitford@rvbadv.example</span>
      </li>
      <li class="contact-item">
        <svg class="contact-icon" viewBox="0 0 20 20" aria-hidden="true"><circle cx="10" cy="10" r="9" fill="var(--orange)"/><circle cx="10" cy="10" r="5.5" fill="none" stroke="var(--navy)" stroke-width="1.3"/><path d="M4.5 10h11M10 4.5c-2.5 3-2.5 8 0 11M10 4.5c2.5 3 2.5 8 0 11" fill="none" stroke="var(--navy)" stroke-width="1.1"/></svg>
        <span>www.<span class="accent">rvbadv</span>.example</span>
      </li>
      <li class="contact-item">
        <svg class="contact-icon" viewBox="0 0 20 20" aria-hidden="true"><path fill="var(--orange)" d="M10 1a6 6 0 0 1 6 6c0 4.5-6 12-6 12S4 11.5 4 7a6 6 0 0 1 6-6z"/><circle cx="10" cy="7" r="2.2" fill="var(--navy)"/></svg>
        <span>2716 5th St. S #4372<br>Arlington, VA 22198</span>
      </li>
    </ul>
  </section>

  <section class="card card-back" aria-label="Business card back">
    <div class="web-band">
      <span class="web-band-text">www.rvbadv.example</span>
    </div>
    <p class="back-brand">Riverbend<br>Advisory</p>
  </section>

</main>
</body>
</html>
```